Hörbuchcover
Zielgruppe
Spiritueller Hörbuchverlag für ganzheitliche Gesundheit, Glück und Wohlstand.
Aufgabenstellung
Benötigt wird ein schönes quadratisches Cover, 2400x2400 mindestens 72dpi für ein Hörbuchcover.
Auf dem Cover soll eine gelb/orange Rose zu in Form einer Blüte zu sehen sein.
Titel: Stille Quellen
Untertitel: Emotionen sind der Schlüssel für Gesundheit, Energie & Lebensfreude
Autorenname: Dr. med. Kathrin Wellbrock
Das Lorvina Logo soll unten mittig sitzen.
Es folgen weiterer Hörbücher von dieser Autorin und es wäre gut wenn man die folgenden Cover in einem ähnlichen Stil halten könnte. Ein harmonisches und gut zu erkennendes Design mit hohem Wiedererkennungseffekt. Ich freue mich auf kreative Designvorschläge.
Auf lorvina.de kann man sehen wo das Logo sitzen soll.
Herzliche Grüße - Jörg

```html
<!DOCTYPE html>
<html lang="de">
<head>
<meta charset="utf-8">
<title>Stille Quellen – Hörbuchcover</title>
<link href="https://fonts.googleapis.com/css2?family=Cinzel:wght@400&family=Crimson+Text&family=Open+Sans:wght@400;600&display=swap" rel="stylesheet">
<style>
  :root {
    --page: #ffffff;
    --violet-deep: #6a1d52;
    --violet: #8a3c86;
    --lilac: #a979c4;
    --cream: #fbf3da;
    --rose-light: #fff6cf;
    --rose-mid: #f5e39a;
    --blush: #e6b8d8;
    --white: #ffffff;
  }
  html, body {
    margin: 0;
    width: 1200px;
    height: 1200px;
    overflow: hidden;
    background: var(--page);
  }
  .cover {
    position: absolute;
    left: 92px;
    top: 92px;
    width: 1016px;
    height: 1016px;
    overflow: hidden;
    background:
      radial-gradient(ellipse 420px 360px at 800px 140px, rgba(255,250,225,0.95), rgba(255,250,225,0) 70%),
      radial-gradient(ellipse 500px 420px at 120px 200px, rgba(138,80,170,0.85), rgba(138,80,170,0) 70%),
      radial-gradient(ellipse 400px 380px at 950px 700px, rgba(220,160,210,0.8), rgba(220,160,210,0) 70%),
      radial-gradient(ellipse 300px 300px at 80px 850px, rgba(200,150,200,0.7), rgba(200,150,200,0) 70%),
      linear-gradient(160deg, #a57cc2 0%, #d9b6d8 45%, #f6e6c8 70%, #e9c3df 100%);
  }
  .rose-photo {
    position: absolute;
    left: 20px;
    top: 350px;
    width: 720px;
    height: 690px;
    border-radius: 50%;
    background: radial-gradient(circle at 50% 48%, var(--rose-light) 0%, var(--rose-mid) 40%, rgba(245,227,154,0.6) 60%, rgba(245,227,154,0) 75%);
  }
  .ornament {
    position: absolute;
    inset: 0;
    width: 1016px;
    height: 1016px;
  }
  .author {
    position: absolute;
    left: 61px;
    top: 56px;
    margin: 0;
    font-family: "Open Sans", sans-serif;
    font-size: 28px;
    color: var(--white);
    letter-spacing: 0.2px;
  }
  .title {
    position: absolute;
    left: 0;
    width: 100%;
    top: 350px;
    margin: 0;
    text-align: center;
    font-family: "Cinzel", serif;
    font-weight: 400;
    font-size: 70px;
    line-height: 90px;
    color: var(--violet-deep);
    letter-spacing: 1px;
  }
  .subtitle {
    position: absolute;
    left: 0;
    width: 100%;
    top: 530px;
    margin: 0;
    text-align: center;
    font-family: "Crimson Text", serif;
    font-size: 39px;
    line-height: 56px;
    color: var(--violet-deep);
    letter-spacing: 0.6px;
  }
  .publisher {
    position: absolute;
    left: 0;
    width: 100%;
    top: 860px;
    text-align: center;
  }
  .publisher-dot {
    display: block;
    margin: 0 auto 8px;
    width: 40px;
    height: 40px;
    border: 3px solid var(--white);
    border-radius: 50%;
    box-sizing: border-box;
  }
  .publisher-name {
    font-family: "Open Sans", sans-serif;
    font-weight: 600;
    font-size: 27px;
    letter-spacing: 6px;
    color: var(--white);
  }
</style>
</head>
<body>
  <main class="cover">
    <div class="rose-photo" role="img" aria-label="Foto einer hellgelben Rosenblüte vor violettem Lichthintergrund"></div>

    <svg class="ornament" viewBox="0 0 1016 1016" aria-hidden="true">
      <path class="swoosh-top" d="M0,88 C240,175 520,120 690,0 C520,150 240,215 0,128 Z" fill="var(--violet)" opacity="0.9"/>
      <ellipse class="title-band" cx="508" cy="391" rx="640" ry="112" fill="var(--cream)" opacity="0.72"/>
      <path class="swoosh-bottom" d="M255,1016 C330,880 560,850 1016,925 L1016,948 C560,875 345,900 280,1016 Z" fill="var(--violet)" opacity="0.9"/>
    </svg>

    <p class="author">Dr. med. Kathrin Wellbrock</p>
    <h1 class="title">STILLE QUELLEN</h1>
    <p class="subtitle">Emotionen sind der Schlüssel für<br>Gesundheit, Energie &amp; Lebensfreude</p>

    <div class="publisher">
      <span class="publisher-dot"></span>
      <span class="publisher-name">LORVINA</span>
    </div>
  </main>
</body>
</html>
```